Webdesign für  FAQ-Finder
Webdesign für FAQ-Finder
Zielgruppe
wiego-lumi.de ist ein FAQ-Finder für werdende / frisch gebackene Eltern in einem ansprechenden, effizienten und modernen Design.
Aufgabenstellung
Ein mobile first Designansatz basierenden auf einem cleanen, modernen Interface und Illustrationen im Stile von:
https://pixelkorb.example/shots/20581934-Tervon-a-fund-for-many
Es gibt noch kein Logo und kein CI. Die Farbwelt soll sich an dem Beispiel von
https://www.quarnetpantry.example/collections
orientieren. Gedeckt, warm. Thematisch geht es um Babies.
For structure perhaps like this:
https://pixelkorb.example/shots/20947715-Flexible-layout-for-Sitewerk-theming-service/attachments/7310452?mode=media
https://pixelkorb.example/shots/20633179--Staffing-Role-locator-Query-App
For Content:
https://www.wiegenpfad.example/category/themen/baby/

```html
<!DOCTYPE html>
<html lang="de">
<head>
<meta charset="utf-8">
<title>wiego-lumi.de – Unsere Themen für Sie</title>
<link rel="stylesheet" href="https://fonts.googleapis.com/css2?family=Poppins:wght@400;500;600;800&display=swap">
<style>
  :root {
    --stage: #dde2ea;
    --screen: #ffffff;
    --ink: #111114;
    --muted: #a3a1ab;
    --brand: #5b3fb9;
    --brand-soft: #c9b8f0;
    --field: #f6f5fb;
    --card-shadow: rgba(90, 70, 160, 0.08);
    --mint: #8fd5b8;
    --blush: #f4c3bb;
    --lilac-wash: #f1eefa;
  }
  * { box-sizing: border-box; margin: 0; padding: 0; }
  html, body {
    width: 1066px; height: 1200px; overflow: hidden;
    background: var(--stage);
    font-family: "Poppins", sans-serif;
  }
  .screen {
    position: absolute; left: 253px; top: 0;
    width: 560px; height: 1200px;
    background: var(--screen);
    overflow: hidden;
  }
  .site-header {
    position: absolute; left: 24px; right: 28px; top: 62px;
    display: flex; justify-content: space-between; align-items: center;
  }
  .brand { display: flex; flex-direction: column; align-items: center; gap: 8px; }
  .brand-dot {
    width: 54px; height: 54px; border-radius: 50%;
    border: 3px solid var(--brand);
  }
  .brand-name { font-size: 25px; font-weight: 400; color: var(--brand); letter-spacing: -0.3px; }
  .menu-toggle { width: 50px; height: 32px; display: flex; flex-direction: column; justify-content: space-between; }
  .menu-toggle span { display: block; height: 3px; background: #2a2a2e; border-radius: 2px; }
  .intro { position: absolute; top: 222px; left: 0; right: 0; text-align: center; }
  .intro h1 {
    font-weight: 800; font-size: 41px; line-height: 1.27;
    letter-spacing: 1.5px; color: var(--ink);
  }
  .intro p {
    margin: 38px auto 0; width: 450px;
    font-size: 15.5px; line-height: 26px; color: var(--muted); letter-spacing: -0.3px;
  }
  .search {
    position: absolute; left: 26px; right: 28px; top: 472px; height: 78px;
    background: var(--field); border-radius: 24px;
    display: flex; align-items: center; justify-content: space-between;
    padding: 0 26px 0 30px;
  }
  .search span { font-size: 19px; color: #6c6a74; }
  .topics {
    position: absolute; top: 606px; left: 0; width: 560px; height: 210px;
  }
  .topic { position: absolute; top: 0; width: 146px; text-align: center; }
  .topic-card {
    width: 146px; height: 137px; border-radius: 32px; background: #fff;
    box-shadow: 0 8px 30px var(--card-shadow);
    display: flex; align-items: center; justify-content: center;
  }
  .topic-icon { width: 58px; height: 58px; border-radius: 16px; background: var(--lilac-wash); border: 3px solid var(--brand-soft); }
  .topic-label { margin-top: 30px; font-size: 18.5px; font-weight: 600; color: var(--ink); letter-spacing: 0.3px; white-space: nowrap; }
  .hero-art {
    position: absolute; left: 80px; top: 838px; width: 410px; height: 362px;
    border-radius: 200px 200px 0 0;
    background: linear-gradient(160deg, var(--lilac-wash) 0%, #d7efe4 45%, var(--mint) 75%, var(--blush) 100%);
  }
</style>
</head>
<body>
  <main class="screen">
    <header class="site-header">
      <div class="brand">
        <span class="brand-dot"></span>
        <span class="brand-name">wiego-lumi.de</span>
      </div>
      <div class="menu-toggle" aria-label="Menü"><span></span><span></span><span></span></div>
    </header>

    <section class="intro">
      <h1>UNSERE THEMEN<br>FÜR SIE</h1>
      <p>Hier finden Sie alle Themen rund um das Baby, die Geburtsvorbereitung, Schwangerschaft, Stillen, den Kinderwunsch und das Familienleben.</p>
    </section>

    <div class="search">
      <span>Suche ..</span>
      <svg width="32" height="32" viewBox="0 0 32 32" fill="none" stroke="#222" stroke-width="2.4" stroke-linecap="round">
        <circle cx="14.5" cy="14.5" r="11"/><line x1="23" y1="23" x2="28" y2="28"/>
      </svg>
    </div>

    <nav class="topics">
      <div class="topic" style="left:-67px">
        <div class="topic-card"><div class="topic-icon" role="img" aria-label="Symbol Kinderwunsch"></div></div>
        <div class="topic-label">Kinderwunsch</div>
      </div>
      <div class="topic" style="left:115px">
        <div class="topic-card"><div class="topic-icon" role="img" aria-label="Symbol Schwangerschaft"></div></div>
        <div class="topic-label">Schwangerschaft</div>
      </div>
      <div class="topic" style="left:296px">
        <div class="topic-card"><div class="topic-icon" role="img" aria-label="Symbol Geburt"></div></div>
        <div class="topic-label">Geburt</div>
      </div>
      <div class="topic" style="left:478px">
        <div class="topic-card"><div class="topic-icon" role="img" aria-label="Symbol Stillen"></div></div>
        <div class="topic-label">Stillen</div>
      </div>
    </nav>

    <div class="hero-art" role="img" aria-label="Illustration: Mutter hält ihr Neugeborenes im Arm, umgeben von grünen Blättern"></div>
  </main>
</body>
</html>
```